Büro Vermietung
Velbrin Design Studio hat eine super Arbeit abgeliefert. Wir sind sehr zufrieden mit der Arbeit und natürlich mit dem Design.
Zielgruppe
Bitte keine weiteren Vorschläge mehr. - Wir haben uns bereits für ein Projekte entschieden.
Aufgabenstellung
Interessenten, welche sich für die Büros oder Gewerbefläche interessieren, sollten auf der Webpage folgende Informationen vorfinden:
Menü-Leiste:
HOME / FLÄCHEN / BILDER / LAGE / KONTAKT
HOME:
Titelbild mit dem Hund & weitblick-raeume.ch + Frontbild Liegenschaft
(Zusatztext folgt noch)
FLAECHEN:
Grundriss & Preise
BILDER:
diverse Bilder (folgen noch)
LAGE:
KONTAKT:
(Unsere Adresse) Vermieter /Kontakt
KARELU IMMOBILEN AG

```html
<!DOCTYPE html>
<html lang="de">
<head>
<meta charset="utf-8">
<title>weitblick-raeume.ch – Flächen</title>
<link href="https://fonts.googleapis.com/css2?family=Architects+Daughter&family=PT+Sans:wght@400;700&display=swap" rel="stylesheet">
<style>
  :root {
    --red: #cc0a2a;
    --red-dark: #a9081f;
    --purple: #4b4a85;
    --price: #56548f;
    --text: #3a3a3a;
    --bg-top: #474686;
    --bg-bottom: #8a88b2;
    --white: #ffffff;
  }
  * { margin: 0; padding: 0; box-sizing: border-box; }
  html, body { width: 1200px; height: 823px; overflow: hidden; }
  body {
    position: relative;
    font-family: "PT Sans", Verdana, sans-serif;
    color: var(--text);
    background: linear-gradient(to bottom, var(--white) 0 152px, var(--bg-top) 152px, var(--bg-bottom) 823px);
  }
  .nav-band {
    position: absolute; left: 0; top: 114px; width: 1200px; height: 38px;
    background: var(--red); border-bottom: 2px solid var(--white);
  }
  .nav { position: absolute; top: 114px; left: 0; width: 1200px; height: 38px; list-style: none; }
  .nav li {
    position: absolute; top: 0; height: 38px; line-height: 38px;
    color: #f4d8dc; font-size: 16px; letter-spacing: 0.3px; transform: translateX(-50%);
    text-align: center;
  }
  .nav li.active {
    color: var(--white); font-weight: 700; background: var(--red-dark);
    width: 92px;
  }
  .page {
    position: absolute; left: 120px; top: 152px; width: 960px; height: 671px;
    background: var(--white);
  }
  .hero {
    position: absolute; left: 122px; top: 152px; width: 956px; height: 200px;
    background: linear-gradient(100deg, #e6e8e6 0%, #d9dcd6 30%, #c9d48e 45%, #dfe2dc 65%, #d2d5d4 100%);
  }
  .hero-fade {
    position: absolute; left: 122px; top: 352px; width: 956px; height: 24px;
    background: linear-gradient(to bottom, #e7e9e4, var(--white));
  }
  .mascot {
    position: absolute; left: 118px; top: 6px; width: 210px; height: 164px;
    background: linear-gradient(to bottom, #c9a27a, #e8e0d4 60%, #e9d56f);
    border-radius: 40px 40px 8px 8px;
  }
  .brand {
    position: absolute; left: 290px; top: 62px;
    font-family: "Architects Daughter", cursive; font-size: 34px; color: var(--purple);
  }
  h1 {
    position: absolute; left: 148px; top: 376px;
    font-family: "Architects Daughter", cursive; font-weight: 400; font-size: 36px; color: var(--purple);
  }
  .intro {
    position: absolute; left: 149px; top: 432px; width: 580px;
    font-size: 13px; line-height: 17px; color: var(--text);
  }
  .offer { position: absolute; left: 149px; width: 310px; font-size: 11.5px; }
  .offer .row { position: relative; height: 17px; line-height: 17px; }
  .offer .label { position: absolute; left: 0; font-weight: 700; letter-spacing: 0.3px; }
  .offer .value { position: absolute; left: 109px; }
  .offer .total {
    position: absolute; right: 0; top: 28px;
    font-size: 17px; color: var(--price);
  }
  .floorplan {
    position: absolute; left: 786px; top: 379px; width: 266px; height: 213px;
    background: linear-gradient(135deg, #b9bbb9, #a9aca9 50%, #c3c5c2);
    border: 2px solid #ecedeb;
  }
  .pdf-button {
    position: absolute; left: 788px; top: 606px; width: 228px; height: 34px;
    background: linear-gradient(to bottom, #e0445c, var(--red));
    color: var(--white); font-size: 12px; line-height: 34px; padding-left: 15px;
  }
  .pdf-arrow {
    position: absolute; left: 1018px; top: 606px; width: 34px; height: 34px;
    background: linear-gradient(to bottom, #e0445c, var(--red));
  }
  .pdf-arrow svg { position: absolute; left: 10px; top: 9px; }
  .footer {
    position: absolute; left: 122px; top: 786px; width: 956px; height: 37px;
    background: var(--red); color: var(--white); font-size: 11.5px;
  }
  .footer .links { position: absolute; left: 27px; top: 11px; }
  .footer .links span { margin: 0 10px; }
  .footer .copy { position: absolute; right: 26px; top: 11px; }
</style>
</head>
<body>
  <div class="nav-band"></div>
  <div class="page"></div>

  <ul class="nav">
    <li style="left:601px">HOME</li>
    <li class="active" style="left:713px">FLÄCHEN</li>
    <li style="left:827px">BILDER</li>
    <li style="left:920px">LAGE</li>
    <li style="left:1015px">KONTAKT</li>
  </ul>

  <div class="hero" role="img" aria-label="Foto eines hellen Grossraumbüros mit Schreibtischen und grünen Bürostühlen"></div>
  <div class="hero-fade"></div>

  <div class="mascot" role="img" aria-label="Illustration des Maskottchens: Hund mit Brille und Krawatte über Büchern"></div>
  <div class="brand">weitblick-raeume.ch</div>

  <h1>Flächen</h1>
  <p class="intro">Lorem ipsum dolor sit amet, consetetur sadipscing elitr, sed diam nonumy eirmod tempor invidunt ut labore et dolore magna aliquyam erat, sed diam voluptua. At vero eos et accusam et justo duo dolores et ea rebum. Stet clita kasd gubergren, no sea takimata sanctus est Lorem ipsum dolor sit amet. Lorem ipsum dolor sit amet, consetetur sadipscing elitr, sed diam nonumy eirmod tempor invidunt ut labore et dolore magn.</p>

  <div class="offer" style="top:532px">
    <div class="row"><span class="label">Fläche:</span><span class="value">1800 m²</span></div>
    <div class="row"><span class="label">Miete / Monat:</span><span class="value">2000,00&nbsp; CF</span></div>
    <div class="row"><span class="label">Nebenkosten:</span><span class="value">&nbsp; 500,00&nbsp; CF</span></div>
    <div class="total">2500,00 CF</div>
  </div>

  <div class="offer" style="top:606px">
    <div class="row"><span class="label">Fläche:</span><span class="value">900 m²</span></div>
    <div class="row"><span class="label">Miete / Monat:</span><span class="value">1200,00&nbsp; CF</span></div>
    <div class="row"><span class="label">Nebenkosten:</span><span class="value">&nbsp; 400,00&nbsp; CF</span></div>
    <div class="total">1600,00 CF</div>
  </div>

  <div class="offer" style="top:682px">
    <div class="row"><span class="label">Fläche:</span><span class="value">300 m²</span></div>
    <div class="row"><span class="label">Miete / Monat:</span><span class="value">500,00&nbsp; CF</span></div>
    <div class="row"><span class="label">Nebenkosten:</span><span class="value">&nbsp; 300,00&nbsp; CF</span></div>
    <div class="total">800,00 CF</div>
  </div>

  <div class="floorplan" role="img" aria-label="Grundriss der Bürofläche mit Arbeitsplätzen"></div>
  <div class="pdf-button">Grundriss als <b>PDF</b> herunterladen</div>
  <div class="pdf-arrow">
    <svg width="14" height="16" viewBox="0 0 14 16"><path d="M3 1 L11 8 L3 15" fill="none" stroke="#fff" stroke-width="3.5"/></svg>
  </div>

  <div class="footer">
    <div class="links">Kontakt<span>|</span>Impressum</div>
    <div class="copy">© 2015 weitblick-raeume.ch</div>
  </div>
</body>
</html>
```